Homebuilder & Remodeling Firm looking for archectrual looking website

We are a Custom home building & remodeling company since 1986 and would like to launch a website.Carl Tondevik the principle of the firm is a graduate of Harwell Univesity school of architecture and draws his own designs and working drawings. and has done many residential, single and multi family projects in the Dallas Ft Worth Metroplex. We want our website to be architectural in design and visually appealing. We will eventually have photos to provide for you. The message we want to communicate is we have current update knowledge with trends, and longevity in experience. Our message is that we are a firm that designs and remodels fully through and we provide a well executed custom home that is unique to each client. The Homes that we build are unique ,authentic and sustainable architectural styles such as mid century modern, contemporary, transitional and they are sophisticated homes to compliment individual lifestyles of our clients. We have a passion for construction and an attention to detail that makes your dreams come to life. We listen to each clients every need in functionality and form and take them from pre-construction to post-construction follow -up.
We help you invest in your home. Thoughts Create Reality

EXAMPLES OF WEBSITES THAT WE LIKE. PLEASE DO
MORE CONTEMPORARY, SLEEK, ARCHITECTURAL

* Please make the LOGO a bigger part of design

http://pellamcrew.build/
https://www.vintrasol.co/
http://dostavanehomes.com/
http://www.milesfardowdesign.com/
http://www.quillmerton.com/
http://fennikdesignstudios.com/about
http://brandelorgc.com/

thank you,

Reason: We have many clients asking to see our website and re ready to launch something for them to look at

Target Market(s)

Home owners, home buyers, interior designers, All ages

Industry/Entity Type

Builders

Coding

Coded - Design and coding required

Number of Pages Required

5+ page

Font styles to use
Sans Serif

Requirements
Must have
• HTML5 OR PHP
• graphic artist must speak English:
• *Visually appealing, user friendly,
• * the website should reflect the stability and integrity of the company since it has been in business for over 30 years
• * a sophistication and refinement is our mandate.
Should not have
• Too busy, too much going on, we want more minimal in design and artsitic

```html
<!DOCTYPE html>
<html lang="en">
<head>
<meta charset="utf-8">
<title>Tavercroft Development — Contact</title>
<link href="https://fonts.googleapis.com/css2?family=Lato:wght@400;700;900&display=swap" rel="stylesheet">
<style>
  :root {
    --navy-deep: #1f2a3d;
    --navy-mid: #3a4862;
    --slate: #5b6a80;
    --white: #ffffff;
    --ink: #111111;
    --nav-grey: #6a6a6a;
    --brand-navy: #1c2c4e;
    --divider: #e6e6e6;
    --field: rgba(226, 228, 234, 0.86);
    --button: #e4e5e9;
  }
  * { margin: 0; padding: 0; box-sizing: border-box; }
  html, body { width: 1200px; height: 577px; overflow: hidden; }
  body {
    position: relative;
    font-family: "Lato", sans-serif;
    background: var(--navy-deep);
  }
  .hero-backdrop {
    position: absolute; inset: 0;
    background:
      linear-gradient(180deg, rgba(60,72,96,0.35) 0%, rgba(20,28,44,0.55) 100%),
      linear-gradient(100deg, #2a3447 0%, #3d4659 35%, #333d52 60%, #4a5670 85%, #56637d 100%);
  }
  .site-header {
    position: absolute; left: 0; top: 0;
    width: 840px; height: 79px;
    background: var(--white);
  }
  .brand {
    position: absolute; left: 34px; top: 22px;
    display: flex; align-items: center; gap: 9px;
  }
  .brand-mark {
    width: 26px; height: 34px;
    background: var(--brand-navy);
  }
  .brand-name {
    font-size: 17px; font-weight: 400;
    color: var(--brand-navy);
    letter-spacing: 0.2px;
  }
  .main-nav a {
    position: absolute; top: 37px;
    font-size: 10.5px; letter-spacing: 2.2px;
    color: var(--nav-grey); text-decoration: none;
    text-transform: uppercase;
  }
  .nav-corner {
    position: absolute; left: 682px; top: 25px;
    width: 8px; height: 8px;
    border-top: 1.5px solid var(--ink); border-left: 1.5px solid var(--ink);
  }
  .nav-divider {
    position: absolute; left: 770px; top: 18px;
    width: 5px; height: 43px; background: var(--divider);
  }
  .share-link {
    position: absolute; left: 790px; top: 35px;
    font-size: 10px; color: var(--ink);
  }
  .contact-title {
    position: absolute; right: 360px; top: 116px;
    font-size: 40px; font-weight: 900; letter-spacing: 1.5px;
    color: var(--white);
  }
  .contact-email {
    position: absolute; right: 360px; top: 181px;
    font-size: 12.5px; font-weight: 700; letter-spacing: 1.3px;
    color: var(--white);
  }
  .contact-form .field {
    position: absolute; left: 312px; width: 528px;
    background: var(--field);
    font-size: 12.5px; color: var(--ink);
    padding: 10px 8px;
  }
  .field-name { top: 239px; height: 45px; padding-top: 15px !important; }
  .field-email { top: 300px; height: 45px; padding-top: 15px !important; }
  .field-message { top: 362px; height: 150px; }
  .send-button {
    position: absolute; left: 313px; top: 530px;
    width: 112px; height: 29px;
    background: var(--button);
    display: flex; align-items: center; justify-content: center; gap: 6px;
    font-size: 14px; font-weight: 900; letter-spacing: 1.2px;
    color: var(--ink);
  }
</style>
</head>
<body>
  <div class="hero-backdrop" role="img" aria-label="Stone-clad custom home with steep gabled roofs under a dusk sky, behind a dark blue overlay"></div>

  <header class="site-header">
    <div class="brand">
      <span class="brand-mark"></span>
      <span class="brand-name">Tavercroft Development</span>
    </div>
    <nav class="main-nav">
      <a href="#" style="left:321px">Home</a>
      <a href="#" style="left:383px">Available Now</a>
      <a href="#" style="left:513px">About Us</a>
      <a href="#" style="left:602px">Affiliate</a>
      <span class="nav-corner"></span>
      <a href="#" style="left:690px">Contact</a>
    </nav>
    <span class="nav-divider"></span>
    <span class="share-link">Share</span>
  </header>

  <h1 class="contact-title">CONTACT US</h1>
  <p class="contact-email">EMAIL:MARTA@TAVERCROFTDEVELOPMENT.COM</p>

  <div class="contact-form">
    <div class="field field-name">Name</div>
    <div class="field field-email">E-mail</div>
    <div class="field field-message">Message</div>
    <div class="send-button">Send
      <svg width="16" height="8" viewBox="0 0 16 8" aria-hidden="true">
        <path d="M0 4H14M10.5 0.8L14.5 4L10.5 7.2" fill="none" stroke="#111" stroke-width="1.6"/>
      </svg>
    </div>
  </div>
</body>
</html>
```